Box design for superfood powders

Hey,
I am creating a new brand of superfoods mixes in and I am looking for a designer to create the design for the box.
I have for 4 products on the roadmap, but I need the design just for the first one:
- For skin nails and hair benefits: Collagen + CoQ10 and Vitamin C powders (eg: Blueberries, Camu Camu, Acai)
- For energy and immune system (eg: mushrooms powder)
- Green Mix (eg: Spirulina + Wheatgrass + Chlorella)
- Protein mix (eg: hemp + rice powders)
I will use Kraft paper for the box so I am able to print max 2 colors on them (black and another color distinctive for each specific powder mix).
I need the design just for the first one with collagen, because all the products will have the same format. I will just change the name, ingredients and the color
More details in the archive attached.

Updates
Low design quality
Target Market(s)
woman between 30-50
Requirements
Should not have
- Ilustrations with fruits or flowers
Just shapes and colors

```html
<!DOCTYPE html>
<html lang="en">
<head>
<meta charset="utf-8">
<title>VELORA — Radiant Collagen packaging</title>
<link rel="stylesheet" href="https://fonts.googleapis.com/css2?family=Poppins:wght@300;700;800&family=Oswald:wght@300;400;500&family=Roboto+Condensed:wght@700&display=swap">
<style>
  :root {
    --kraft: #bb8f64;
    --kraft-dark: #a97c53;
    --ink: #111111;
    --purple: #3b2a78;
    --band: #4a3b86;
    --white: #ffffff;
    --page: #ffffff;
  }
  html, body {
    margin: 0;
    width: 1200px;
    height: 1200px;
    overflow: hidden;
    background: var(--page);
  }
  .canvas { position: relative; width: 1200px; height: 1200px; }

  .brand-lockup {
    position: absolute;
    left: 140px;
    top: 255px;
    width: 340px;
    text-align: center;
  }
  .brand-name {
    font-family: "Oswald", sans-serif;
    font-weight: 500;
    font-size: 92px;
    line-height: 1;
    letter-spacing: 6px;
    color: var(--ink);
  }
  .brand-tagline {
    margin-top: 20px;
    font-family: "Roboto Condensed", sans-serif;
    font-weight: 700;
    font-size: 19px;
    letter-spacing: 2.4px;
    color: var(--ink);
  }

  .sachet { position: absolute; left: 60px; top: 590px; width: 480px; height: 480px; }

  .box-side {
    position: absolute;
    left: 570px;
    top: 140px;
    width: 150px;
    height: 930px;
    background: var(--kraft);
    box-sizing: border-box;
    border-right: 1px solid var(--kraft-dark);
  }
  .box-front { position: absolute; left: 720px; top: 140px; width: 400px; height: 930px; }

  .side-brand { position: absolute; top: 118px; left: 0; width: 150px; text-align: center; }
  .side-brand-name {
    font-family: "Oswald", sans-serif;
    font-weight: 500;
    font-size: 36px;
    line-height: 1;
    letter-spacing: 2px;
    color: var(--ink);
  }
  .side-brand-tagline {
    margin-top: 8px;
    font-family: "Roboto Condensed", sans-serif;
    font-weight: 700;
    font-size: 8px;
    letter-spacing: 0.6px;
    color: var(--ink);
  }
  .side-copy {
    position: absolute;
    top: 235px;
    left: 12px;
    width: 126px;
    font-family: "Oswald", sans-serif;
    font-weight: 300;
    font-size: 10.5px;
    line-height: 1.55;
    color: var(--ink);
    text-align: center;
  }
  .side-copy p { margin: 0 0 20px; }
  .side-copy .intro { text-align: justify; text-align-last: center; }
  .side-copy .label { font-weight: 400; display: block; }
  .side-band {
    position: absolute;
    left: 0;
    top: 875px;
    width: 150px;
    height: 50px;
    background: var(--band);
    display: flex;
    align-items: center;
    justify-content: center;
    font-family: "Oswald", sans-serif;
    font-weight: 500;
    font-size: 9.5px;
    color: var(--white);
  }

  .display { font-family: "Poppins", sans-serif; }
  .condensed { font-family: "Oswald", sans-serif; }
  .tag { font-family: "Roboto Condensed", sans-serif; font-weight: 700; }
</style>
</head>
<body>
<main class="canvas">

  <section class="brand-lockup">
    <div class="brand-name">VELORA</div>
    <div class="brand-tagline">Nourish your everyday glow</div>
  </section>

  <svg class="sachet" viewBox="0 0 480 480" xmlns="http://www.w3.org/2000/svg">
    <defs>
      <radialGradient id="dotsSoft" cx="50%" cy="50%" r="50%">
        <stop offset="0%" stop-color="#2a1f18" stop-opacity="0.10"/>
        <stop offset="70%" stop-color="#2a1f18" stop-opacity="0.28"/>
        <stop offset="100%" stop-color="#2a1f18" stop-opacity="0.05"/>
      </radialGradient>
      <clipPath id="sachetClip"><rect x="0" y="0" width="480" height="480"/></clipPath>
    </defs>
    <g clip-path="url(#sachetClip)">
      <rect x="0" y="0" width="480" height="480" fill="var(--kraft)"/>
      <rect x="0" y="0" width="480" height="30" fill="var(--kraft-dark)"/>
      <rect x="0" y="450" width="480" height="30" fill="var(--kraft-dark)"/>
      <path d="M406 0 H480 V74 A74 74 0 0 0 406 0 Z" fill="var(--ink)"/>
      <circle role="img" aria-label="Halftone dot pattern" cx="425" cy="60" r="80" fill="url(#dotsSoft)"/>
      <circle role="img" aria-label="Halftone dot pattern" cx="0" cy="211" r="45" fill="url(#dotsSoft)"/>
      <circle cx="420" cy="125" r="20" fill="var(--purple)"/>

      <text class="condensed" x="243" y="106" text-anchor="middle" font-weight="500" font-size="44" letter-spacing="3" fill="var(--ink)">VELORA</text>
      <text class="tag" x="243" y="127" text-anchor="middle" font-size="9" letter-spacing="1.4" fill="var(--ink)">Nourish your everyday glow</text>

      <text class="display" x="71" y="216" font-weight="800" font-size="70" textLength="339" lengthAdjust="spacingAndGlyphs" fill="var(--ink)">RADIANT</text>
      <text class="display" x="145" y="256" font-weight="300" font-size="36" textLength="190" lengthAdjust="spacingAndGlyphs" fill="var(--purple)">COLLAGEN</text>

      <g fill="none" stroke="var(--ink)" stroke-width="1.2">
        <circle cx="94" cy="308" r="21"/><circle cx="142" cy="308" r="21"/><circle cx="191" cy="308" r="21"/>
        <circle cx="239" cy="308" r="21"/><circle cx="288" cy="308" r="21"/><circle cx="336" cy="308" r="21"/>
        <circle cx="385" cy="308" r="21"/>
      </g>
      <g class="condensed" font-size="6.5" font-weight="500" fill="var(--ink)" text-anchor="middle">
        <text x="94" y="306">GLUTEN</text><text x="94" y="315">FREE</text>
        <text x="142" y="306">DAIRY</text><text x="142" y="315">FREE</text>
        <text x="191" y="306">SOY</text><text x="191" y="315">FREE</text>
        <text x="239" y="306">GMO</text><text x="239" y="315">FREE</text>
        <text x="288" y="306">SUGAR</text><text x="288" y="315">FREE</text>
        <text x="336" y="303">NO ART.</text><text x="336" y="311">FLAVORS</text>
        <text x="385" y="306">PRESERV.</text><text x="385" y="315">FREE</text>
      </g>

      <rect x="0" y="368" width="480" height="48" fill="var(--band)"/>
      <text class="display" x="71" y="398" font-weight="700" font-size="14.5" fill="var(--white)">COQ10 AND VITAMIN C POWDERS</text>
      <circle cx="382" cy="392" r="38" fill="var(--ink)" stroke="var(--kraft)" stroke-width="2"/>
      <text class="condensed" x="382" y="388" text-anchor="middle" font-size="10.5" font-weight="500" fill="var(--white)">14 PORTIONS</text>
      <text class="condensed" x="382" y="402" text-anchor="middle" font-size="10.5" font-weight="500" fill="var(--white)">X 10G = 140G</text>
    </g>
  </svg>

  <section class="box-side">
    <div class="side-brand">
      <div class="side-brand-name">VELORA</div>
      <div class="side-brand-tagline">Nourish your everyday glow</div>
    </div>
    <div class="side-copy">
      <p class="intro">We make it easy for busy people to look and feel good about their appearance. Just add Radiant Collagen powder to your favorite smoothie or milk and get the extra dose of collagen and skin protecting antioxidants. It helps combat the effects of free radicals and may restore your natural plumpness.</p>
      <p><span class="label">FREE FROM:</span>Gluten, Dairy, Soy, GMO, sweeteners, flavours, additives, preservatives or anything artificial.</p>
      <p><span class="label">HOW TO USE IT:</span>Add one pack to your water, smoothies, yoghurt, musli, oatmeal</p>
      <p><span class="label">STORAGE:</span>Keep closed in a cool dry place</p>
      <p><span class="label">PRODUCED BY:</span>Norrin SRL for Brightpath SRL</p>
      <p><span class="label">CONNECT:</span>Call +40 111 222 333 or visit our website velora-example.com</p>
    </div>
    <div class="side-band">COQ10 AND VITAMIN C POWDERS</div>
  </section>

  <svg class="box-front" viewBox="0 0 400 930" xmlns="http://www.w3.org/2000/svg">
    <defs>
      <radialGradient id="dotsSoftBox" cx="50%" cy="50%" r="50%">
        <stop offset="0%" stop-color="#2a1f18" stop-opacity="0.10"/>
        <stop offset="70%" stop-color="#2a1f18" stop-opacity="0.28"/>
        <stop offset="100%" stop-color="#2a1f18" stop-opacity="0.05"/>
      </radialGradient>
      <clipPath id="frontClip"><rect x="0" y="0" width="400" height="930"/></clipPath>
    </defs>
    <g clip-path="url(#frontClip)">
      <rect x="0" y="0" width="400" height="930" fill="var(--kraft)"/>
      <path d="M250 0 H400 V150 A150 150 0 0 0 250 0 Z" fill="var(--ink)"/>
      <circle role="img" aria-label="Halftone dot pattern" cx="306" cy="131" r="95" fill="url(#dotsSoftBox)"/>
      <circle cx="292" cy="254" r="36" fill="var(--purple)"/>

      <text class="display" transform="rotate(-90)" x="-650" y="118" font-weight="800" font-size="118" textLength="603" lengthAdjust="spacingAndGlyphs" fill="var(--ink)">RADIANT</text>
      <text class="display" transform="rotate(-90)" x="-384" y="178" font-weight="300" font-size="60" textLength="331" lengthAdjust="spacingAndGlyphs" fill="var(--purple)">COLLAGEN</text>

      <circle cx="322" cy="597" r="49" fill="var(--ink)"/>
      <text class="condensed" x="322" y="594" text-anchor="middle" font-size="13" font-weight="500" fill="var(--white)">14 PORTIONS</text>
      <text class="condensed" x="322" y="611" text-anchor="middle" font-size="13" font-weight="500" fill="var(--white)">X 10G = 140G</text>

      <text class="condensed" x="269" y="733" text-anchor="middle" font-weight="500" font-size="62" letter-spacing="4" fill="var(--ink)">VELORA</text>
      <text class="tag" x="269" y="763" text-anchor="middle" font-size="12.5" letter-spacing="1.6" fill="var(--ink)">Nourish your everyday glow</text>

      <g fill="none" stroke="var(--ink)" stroke-width="1.2">
        <circle cx="50" cy="825" r="22"/><circle cx="100" cy="825" r="22"/><circle cx="150" cy="825" r="22"/>
        <circle cx="200" cy="825" r="22"/><circle cx="250" cy="825" r="22"/><circle cx="300" cy="825" r="22"/>
        <circle cx="350" cy="825" r="22"/>
      </g>
      <g class="condensed" font-size="6.8" font-weight="500" fill="var(--ink)" text-anchor="middle">
        <text x="50" y="823">GLUTEN</text><text x="50" y="832">FREE</text>
        <text x="100" y="823">DAIRY</text><text x="100" y="832">FREE</text>
        <text x="150" y="823">SOY</text><text x="150" y="832">FREE</text>
        <text x="200" y="823">GMO</text><text x="200" y="832">FREE</text>
        <text x="250" y="823">SUGAR</text><text x="250" y="832">FREE</text>
        <text x="300" y="820">NO ART.</text><text x="300" y="829">FLAVORS</text>
        <text x="350" y="823">PRESERV.</text><text x="350" y="832">FREE</text>
      </g>

      <rect x="0" y="875" width="400" height="50" fill="var(--band)"/>
      <text class="display" x="200" y="906" text-anchor="middle" font-weight="700" font-size="16" fill="var(--white)">COQ10 AND VITAMIN C POWDERS</text>
    </g>
  </svg>

</main>
</body>
</html>
```